# We are a digital advertising company who provides technological solutions to publisher and advertisers.
# We do affiliate (performance) marketing, mobile & display advertising and XML Advertising
# We want to get a design for our business card
# We want the design to be creative , clear about what we provide to our customers ,not too simple, and if possible,
#You can try some space on the back side for our customers to take note (that part can be a bit funny & creative) (space not obligatory)
#If you have more creative ideas we would like to see it.

We already have a logo and we will use it in the card. You can find it attached.

You can prepare the business card with a default name and the title is Founder, Sevda Korkmaz

for the card:
Founder : Sevda Korkmaz
email: sevda@[login to view URL]
phone:+905328470256

```html
<!DOCTYPE html>
<html lang="en">
<head>
<meta charset="utf-8">
<title>Novareach Business Card</title>
<link href="https://fonts.googleapis.com/css2?family=Montserrat:wght@400;600;800&display=swap" rel="stylesheet">
<style>
  :root {
    --backdrop: #3a3b3e;
    --card: #262d3b;
    --green: #5c9e3b;
    --green-light: #70b644;
    --white: #ffffff;
  }
  * { margin: 0; padding: 0; box-sizing: border-box; }
  html, body {
    width: 1200px; height: 900px; overflow: hidden;
    background: var(--backdrop);
    font-family: "Montserrat", Arial, sans-serif;
  }
  .sheet { position: relative; width: 1200px; height: 900px; }
  .card {
    position: absolute; left: 250px; width: 700px; height: 400px;
    background: var(--card); border-radius: 26px; overflow: hidden;
    box-shadow: 0 12px 30px rgba(0,0,0,.35);
  }
  .card--front { top: 30px; }
  .card--back { top: 470px; }
  .card__wave { position: absolute; inset: 0; width: 700px; height: 400px; }
  .brand { position: absolute; display: flex; align-items: center; gap: 18px; white-space: nowrap; }
  .brand__mark {
    flex: none; border-radius: 50%;
    background: linear-gradient(135deg, var(--green-light), var(--green));
  }
  .brand__name {
    font-weight: 800; color: var(--green-light); letter-spacing: 1px; line-height: 1;
  }
  .brand__sub {
    color: var(--white); font-size: 12px; letter-spacing: 2px; font-weight: 400; margin-top: 6px;
  }
  .card--front .brand { left: 150px; top: 112px; }
  .card--front .brand__mark { width: 80px; height: 80px; }
  .card--front .brand__name { font-size: 44px; }
  .tagline {
    position: absolute; left: 248px; top: 200px;
    color: var(--white); font-size: 18px; letter-spacing: .5px; white-space: nowrap;
  }
  .card--back .brand { left: 320px; top: 82px; gap: 14px; }
  .card--back .brand__mark { width: 58px; height: 58px; }
  .card--back .brand__name { font-size: 30px; }
  .card--back .brand__sub { font-size: 9px; }
  .accent-dot { position: absolute; border-radius: 50%; background: var(--green-light); }
  .signal-dot { width: 22px; height: 22px; }
  .trail-dot { width: 16px; height: 16px; }
  .card--front .signal-dot { left: 640px; top: 96px; }
  .card--front .trail-dot { left: 596px; top: 170px; }
  .card--back .signal-dot { left: 645px; top: 128px; }
  .card--back .trail-dot { left: 572px; top: 196px; }
  .person { position: absolute; left: 58px; top: 160px; }
  .person__name { color: var(--green-light); font-weight: 800; font-size: 30px; }
  .person__title { color: var(--white); font-size: 20px; margin-top: 4px; }
  .contacts { position: absolute; left: 58px; top: 245px; list-style: none; }
  .contacts li {
    display: flex; align-items: center; gap: 16px;
    color: var(--white); font-size: 20px; margin-bottom: 20px;
  }
  .contacts svg { width: 20px; height: 20px; fill: var(--green-light); }
</style>
</head>
<body>
<main class="sheet">
  <section class="card card--front" aria-label="Card front">
    <svg class="card__wave" viewBox="0 0 700 400" aria-hidden="true">
      <defs>
        <linearGradient id="waveGreen" x1="0" y1="0" x2="1" y2="1">
          <stop offset="0" stop-color="#70b644"/><stop offset="1" stop-color="#4f8f32"/>
        </linearGradient>
      </defs>
      <path d="M0,365 C280,350 500,260 640,140 C665,118 685,112 700,112 L700,400 L0,400Z" fill="url(#waveGreen)"/>
      <path d="M0,332 C250,320 440,258 585,165 C455,268 260,334 0,345Z" fill="url(#waveGreen)"/>
    </svg>
    <div class="brand">
      <div class="brand__mark" role="img" aria-label="Brand symbol"></div>
      <div>
        <div class="brand__name">NOVAREACH</div>
        <div class="brand__sub">GLOBAL ADNETWORK</div>
      </div>
    </div>
    <p class="tagline">“Affiliate, Mobile, XML, Self Serve”</p>
    <div class="accent-dot signal-dot" role="img" aria-label="Signal decoration"></div>
    <div class="accent-dot trail-dot" role="img" aria-label="Small brand decoration"></div>
  </section>

  <section class="card card--back" aria-label="Card back">
    <svg class="card__wave" viewBox="0 0 700 400" aria-hidden="true">
      <path d="M0,372 C290,355 510,270 645,165 C668,148 686,142 700,142 L700,400 L0,400Z" fill="url(#waveGreen)"/>
      <path d="M0,342 C260,328 450,268 590,185 C460,285 265,345 0,355Z" fill="url(#waveGreen)"/>
    </svg>
    <div class="brand">
      <div class="brand__mark" role="img" aria-label="Brand symbol"></div>
      <div>
        <div class="brand__name">NOVAREACH</div>
        <div class="brand__sub">GLOBAL ADNETWORK</div>
      </div>
    </div>
    <div class="accent-dot signal-dot" role="img" aria-label="Signal decoration"></div>
    <div class="accent-dot trail-dot" role="img" aria-label="Small brand decoration"></div>
    <div class="person">
      <div class="person__name">Sevda Korkmaz</div>
      <div class="person__title">Founder</div>
    </div>
    <ul class="contacts">
      <li>
        <svg viewBox="0 0 24 24" aria-hidden="true"><path d="M2 11 22 3 15 22 11 14Z"/></svg>
        sevda@[login to view URL]
      </li>
      <li>
        <svg viewBox="0 0 24 24" aria-hidden="true"><path d="M6.6 10.8a15 15 0 0 0 6.6 6.6l2.2-2.2a1 1 0 0 1 1-.25 11 11 0 0 0 3.6.6 1 1 0 0 1 1 1V20a1 1 0 0 1-1 1A17 17 0 0 1 3 4a1 1 0 0 1 1-1h3.5a1 1 0 0 1 1 1 11 11 0 0 0 .6 3.6 1 1 0 0 1-.25 1Z"/></svg>
        +905328470256
      </li>
    </ul>
  </section>
</main>
</body>
</html>
```